Poem Handwritten by Veteran while in the jungle of Vietnam

My parents are celebrating their 50th wedding anniversary this year. I wanted to give them a very memorable gift. On my parents 2nd anniversary, my father was stationed in Vietnam. On that night he was in the jungle waiting till morning and wrote a poem to my mother using his pant leg as paper. I would like this poem to typographically designed to be framed and hung on the wall.

I have attached a picture of the poem below. It will need to be 11x14 when printed for framing. It would be great if there was background or artwork to make it more visually interesting, perhaps in a watercolor. My parents have a transitional style. I have attached some possible color schemes as well. Cool greens, blue, neutral grays, with hints of berries or highlights of yellow. These are just a guide, I would be open to your interpretations.

Thank you for your help. This will hopefully be a gift they will truly treasure as much as the poem itself.

Target Market(s)

My parents who are excited to be celebrating their 50th wedding anniversary. It should have a transitional, mature style.

Font styles to use
Serif
Script

Requirements
Must have
• The poem, typographically designed. There can be a mix of fonts, but legibility is critically important.
• Now that some designs have come through I wanted to give some more guidance of what I'm looking for. I want something that feels sophisticated and artistic.
Nice to have
• A background or art work, using the color schemes attached as a guide. I am really liking the designs that have a full color landscape artwork in the background. The fonts should be elegant and formal. I really like the romantic, muted colors. I had trouble finding similar projects online in the style I wanted until I cam across wedding invites. Those seem to be the most applicable. I've added pictures of some so you can get a sense of what I'm looking for. I am really liking the jungle foliage, starry skies or sunrises.
Should not have
• Cartoon caricatures, fonts that are too illegible when printed. I'm not liking anything whimsical. I don't like the very bright colors for this project.

```html
<!DOCTYPE html>
<html lang="en">
<head>
<meta charset="utf-8">
<title>Walter's Anniversary Poem</title>
<link href="https://fonts.googleapis.com/css2?family=Dancing+Script:wght@500;700&family=Questrial&display=swap" rel="stylesheet">
<style>
  :root {
    --backdrop: #eeeeec;
    --forest: #2b4b3d;
    --forest-deep: #1d3a2c;
    --paper: #efe3e0;
    --ink: #2a2523;
    --gold: #c99a68;
    --sand: #dcbfa2;
  }
  * { margin: 0; padding: 0; box-sizing: border-box; }
  html, body {
    width: 1107px; height: 1200px; overflow: hidden;
    background: var(--backdrop);
  }
  .poster {
    position: absolute; left: 120px; top: 20px;
    width: 866px; height: 1160px;
    background: var(--forest);
    overflow: hidden;
  }
  .wash { position: absolute; inset: 0; width: 100%; height: 100%; }
  .poem-card {
    position: absolute; left: 101px; top: 149px;
    width: 660px; height: 848px;
    background: var(--paper);
    border-radius: 95px 0 70px 0;
    color: var(--ink);
  }
  .divider {
    position: absolute; left: 344px; top: 55px;
    width: 1.5px; height: 715px; background: var(--gold);
  }
  .title {
    position: absolute; right: 320px; top: 40px;
    font-family: "Dancing Script", cursive; font-weight: 700;
    font-size: 42px; line-height: 56px; text-align: right;
  }
  .title .underline {
    display: inline-block; border-bottom: 2px solid var(--ink); line-height: 52px;
  }
  .stanza { position: absolute; white-space: nowrap; }
  .stanza.left { right: 330px; text-align: right; }
  .stanza.right { left: 358px; text-align: left; }
  .stanza.plain {
    font-family: "Questrial", sans-serif; font-size: 15px; line-height: 21.5px;
  }
  .stanza.script {
    font-family: "Dancing Script", cursive; font-weight: 500;
    font-size: 19px; line-height: 26px;
  }
  .dateline {
    position: absolute; left: 0; right: 0; top: 800px; text-align: center;
    font-family: "Questrial", sans-serif; font-size: 15px; letter-spacing: 0.5px;
  }
  .ornaments { position: absolute; inset: 0; width: 100%; height: 100%; pointer-events: none; }
</style>
</head>
<body>
  <div class="poster">
    <svg class="wash" viewBox="0 0 866 1160" role="img" aria-label="Dark green watercolour washes behind the poem">
      <defs>
        <radialGradient id="washTone" cx="50%" cy="50%" r="50%">
          <stop offset="0%" stop-color="#183427"/>
          <stop offset="70%" stop-color="#1d3a2c"/>
          <stop offset="100%" stop-color="#2b4b3d" stop-opacity="0"/>
        </radialGradient>
      </defs>
      <ellipse cx="660" cy="220" rx="230" ry="220" fill="url(#washTone)"/>
      <ellipse cx="120" cy="560" rx="120" ry="420" fill="url(#washTone)"/>
      <ellipse cx="430" cy="1060" rx="360" ry="110" fill="url(#washTone)"/>
      <ellipse cx="230" cy="130" rx="110" ry="90" fill="url(#washTone)"/>
    </svg>

    <svg class="ornaments" viewBox="0 0 866 1160">
      <circle cx="25" cy="0" r="65" fill="var(--sand)"/>
      <circle cx="835" cy="1160" r="65" fill="var(--sand)"/>
      <g fill="var(--gold)">
        <circle cx="118" cy="24" r="11"/><circle cx="163" cy="33" r="8"/>
        <circle cx="94" cy="60" r="8"/><circle cx="130" cy="70" r="7"/>
        <circle cx="150" cy="90" r="10"/><circle cx="52" cy="103" r="7"/>
        <circle cx="75" cy="120" r="5"/><circle cx="100" cy="112" r="6"/>
        <circle cx="118" cy="145" r="5"/>
        <circle cx="748" cy="1136" r="11"/><circle cx="700" cy="1125" r="8"/>
        <circle cx="770" cy="1098" r="8"/><circle cx="735" cy="1090" r="7"/>
        <circle cx="712" cy="1070" r="10"/><circle cx="812" cy="1058" r="7"/>
        <circle cx="790" cy="1040" r="5"/><circle cx="765" cy="1048" r="6"/>
        <circle cx="745" cy="1015" r="5"/>
      </g>
      <g role="img" aria-label="Gold leafy branch sprig">
        <ellipse cx="215" cy="225" rx="175" ry="22" transform="rotate(-25 215 225)" fill="var(--gold)" opacity="0.55"/>
      </g>
      <g role="img" aria-label="Gold leafy branch sprig">
        <ellipse cx="640" cy="960" rx="170" ry="22" transform="rotate(-30 640 960)" fill="var(--gold)" opacity="0.55"/>
      </g>
    </svg>

    <div class="poem-card">
      <div class="divider"></div>

      <h1 class="title">Walter’s<br><span class="underline">Anniversary Poem</span></h1>

      <div class="stanza left plain" style="top:184px">Life’s journey began with a challenge,<br>It was heralded far and near.<br>The road led on forever,<br>Its completion was known to be dear.</div>
      <div class="stanza left script" style="top:297px">From the garden of light it proceeded,<br>To the valley of shadows it led.<br>Thorns and thistles adorned it,<br>Past abyss and crevice it sped.</div>
      <div class="stanza left plain" style="top:433px">The brave surged forward with courage,<br>The wise undaunted pressed on.<br>The mightly held high their banner,<br>We all awaited the dawn.</div>
      <div class="stanza left script" style="top:550px">Though the pitfalls and hazards were many,<br>The pathway was clearly in view.<br>Straight and sure it glided,<br>Its course we knew to be true.</div>
      <div class="stanza left plain" style="top:681px">I knew you, Sweetheart, beforehand,<br>So precious and sweet were you.<br>Our moments of bliss were priceless,<br>Each day brought us joy anew.</div>

      <div class="stanza right script" style="top:57px">The call to progression beckoned,<br>At last I would have my chance—<br>To clasp you to me forever,<br>And seal our divine romance.</div>
      <div class="stanza right plain" style="top:188px">I eagerly started the journey,<br>Though with sorrow, I left you behind.<br>With courage and faith I countinued,<br>For I knew, that you later I’d find.</div>
      <div class="stanza right script" style="top:298px">I diligently searched for you, Darling,<br>The roadway was both bleak and fair.<br>Though the years grew long in number,<br>I did not give up in despair.</div>
      <div class="stanza right plain" style="top:433px">At last in the distance I saw you,<br>So beautiful, lovely, and sweet!<br>Your attention I struggled to capture,<br>Your love I wrested to meet.</div>
      <div class="stanza right script" style="top:550px">What rapture was mine in fulfillment,<br>As now together we stand.<br>To cherish and love each other,<br>While our plans and dreams expand.</div>
      <div class="stanza right plain" style="top:681px">I love you darling, forever,<br>My life you have made replete.<br>Our eternal mansion beckons,<br>Your love has made it complete.</div>

      <p class="dateline">20 JULY 1970, MONDAY, LZ RIDGEWAY</p>
    </div>
  </div>
</body>
</html>
```